Kestrel Photography Business Card

I need a business card designed for a photography business based in Perth, Western Australia called Kestrel Photography.

We specialise in wedding, event photography and portrait photography.

The business card must borrow the style of the attached logo.

The hex codes for the colours in the logo are:
#ED1D85 - Pink
#89C23E - Green
#37282F - Black

The name on the card will be:
Name: Toviran
Phone: 0417395268
Website: www.kestrelphotography.com.au
Friendsphere: kestrelphotography

I am open and happy to accept creative concepts.

I’d like some space at the back for writing notes and appointment details.

```html
<!DOCTYPE html>
<html lang="en">
<head>
<meta charset="utf-8">
<title>Kestrel Photography Business Card</title>
<link rel="stylesheet" href="https://fonts.googleapis.com/css2?family=Lato:wght@400;700&family=Raleway:wght@400;600&display=swap">
<style>
  :root {
    --pink: #ED1D85;
    --pink-soft: #e0559c;
    --green: #89C23E;
    --green-soft: #b5d96a;
    --ink: #37282F;
    --grey: #6f6a6c;
    --paper: #ffffff;
    --backdrop: #e9e7e4;
    --rule: #2c2f6b;
  }
  * { box-sizing: border-box; margin: 0; padding: 0; }
  html, body { width: 1200px; height: 1000px; overflow: hidden; }
  body { background: var(--backdrop); font-family: "Lato", sans-serif; position: relative; }

  .card {
    position: absolute; left: 190px; width: 820px; height: 455px;
    background: var(--paper); overflow: hidden;
    box-shadow: 0 2px 8px rgba(0,0,0,.12);
  }
  .card--back { top: 30px; }
  .card--front { top: 515px; }

  /* Back: appointment card */
  .decor-panel {
    position: absolute; left: 0; top: 0; width: 260px; height: 455px;
    background: radial-gradient(ellipse at 30% 40%, rgba(237,29,133,.14), rgba(137,194,62,.10) 55%, rgba(255,255,255,0) 80%);
  }
  .appt-title {
    position: absolute; top: 34px; left: 0; width: 100%; text-align: center;
    font-family: "Raleway", sans-serif; font-weight: 600; font-size: 28px;
    letter-spacing: 2px; color: var(--pink-soft);
  }
  .weekdays {
    position: absolute; top: 96px; left: 130px; display: flex; gap: 34px;
    font-weight: 700; font-size: 19px; color: var(--green-soft);
  }
  .appt-line {
    position: absolute; font-size: 24px; color: var(--pink-soft); font-family: "Raleway", sans-serif; font-weight: 600;
    display: flex; align-items: flex-end; gap: 6px;
  }
  .appt-line--date { top: 150px; left: 130px; }
  .blank { display: inline-block; border-bottom: 1.5px solid var(--ink); height: 24px; }
  .ampm { color: var(--green); }
  .ampm span { color: var(--pink); }
  .appt-for {
    position: absolute; top: 206px; left: 150px; width: 430px;
    border-bottom: 1.5px solid var(--rule); text-align: center;
    font-size: 14px; color: var(--pink-soft); padding-bottom: 16px;
  }
  .appt-note {
    position: absolute; top: 250px; left: 150px; width: 430px; text-align: center;
    font-size: 15px; font-weight: 700; color: var(--pink); line-height: 1.2;
  }
  .appt-rule { position: absolute; top: 294px; left: 150px; width: 430px; border-bottom: 1.5px solid var(--rule); }
  .brand-mark { width: 56px; height: 56px; border-radius: 50%; background: var(--pink); }
  .brand-name {
    font-family: "Raleway", sans-serif; font-size: 14px; letter-spacing: 6px;
    color: var(--grey); text-transform: uppercase; white-space: nowrap;
  }
  .card--back .brand-mark { position: absolute; right: 80px; top: 200px; }
  .card--back .brand-name { position: absolute; right: 30px; top: 312px; }
  .web-band {
    position: absolute; right: 0; bottom: 60px; width: 470px; height: 52px;
    background: var(--pink); color: #fff; display: flex; align-items: center; justify-content: center;
    font-family: "Raleway", sans-serif; font-size: 15px; letter-spacing: 4px;
  }
  .social {
    position: absolute; left: 40px; bottom: 50px; display: flex; align-items: center; gap: 12px;
  }
  .social-square { width: 58px; height: 50px; border-radius: 8px; background: var(--pink-soft); }
  .social-text { color: var(--pink); line-height: 1; }
  .social-text .lead { font-size: 17px; }
  .social-text .network { font-size: 27px; }
  .social-text .url { font-size: 9px; color: var(--grey); }

  /* Front: contact card */
  .front-shapes { position: absolute; inset: 0; }
  .brand { position: absolute; display: flex; flex-direction: column; align-items: center; gap: 10px; }
  .card--front .brand { right: 60px; top: 28px; }
  .tagline {
    position: absolute; right: 40px; top: 140px; width: 420px; text-align: center;
    font-family: "Raleway", sans-serif; font-weight: 600; font-size: 12px;
    letter-spacing: 2.5px; color: var(--green); line-height: 1.35;
  }
  .person { position: absolute; right: 60px; top: 255px; text-align: right; }
  .person-name { font-family: "Raleway", sans-serif; font-weight: 600; font-size: 30px; letter-spacing: 4px; color: var(--ink); }
  .person-role { font-size: 24px; color: var(--pink); letter-spacing: 1px; }
  .contacts { position: absolute; left: 42px; top: 290px; list-style: none; color: #fff; font-size: 22px; font-weight: 700; }
  .contacts li { display: flex; align-items: center; gap: 10px; height: 38px; }
  .contacts svg { width: 18px; height: 18px; }
  .icon-square { width: 16px; height: 16px; background: #fff; border-radius: 2px; }
</style>
</head>
<body>

<section class="card card--back" aria-label="Appointment card, back">
  <div class="decor-panel" role="img" aria-label="Faint floral decoration in pink and green"></div>
  <h2 class="appt-title">Next Appointment</h2>
  <div class="weekdays"><span>Sun</span><span>Mon</span><span>Tue</span><span>Wed</span><span>Thu</span><span>Fri</span><span>Sat</span></div>
  <div class="appt-line appt-line--date">
    Date :<span class="blank" style="width:150px"></span>at<span class="blank" style="width:150px"></span><span class="ampm">pm<span>/</span>am</span>
  </div>
  <div class="appt-for">for</div>
  <p class="appt-note">If unable to keep appointment kindly<br>give a 24 hour notice.</p>
  <div class="appt-rule"></div>
  <div class="brand-mark"></div>
  <div class="brand-name">Kestrel Photography</div>
  <div class="web-band">WWW.KESTRELPHOTOGRAPHY.COM.AU</div>
  <div class="social">
    <div class="social-square"></div>
    <div class="social-text">
      <div class="lead">Join us on</div>
      <div class="network">Friendsphere</div>
      <div class="url">www.friendsphere.com/kestrelphotography</div>
    </div>
  </div>
</section>

<section class="card card--front" aria-label="Business card, front">
  <svg class="front-shapes" viewBox="0 0 820 455" preserveAspectRatio="none" aria-hidden="true">
    <path d="M0,150 Q350,60 640,455 L0,455 Z" fill="var(--green-soft)"/>
    <path d="M0,178 Q330,95 610,455 L0,455 Z" fill="#fff"/>
    <path d="M0,186 Q325,105 598,455 L0,455 Z" fill="var(--pink)"/>
  </svg>
  <div class="brand">
    <div class="brand-mark"></div>
    <div class="brand-name">Kestrel Photography</div>
  </div>
  <p class="tagline">WE SPECIALISE IN WEDDING, EVENT PHOTOGRAPHY AND PORTRAIT PHOTOGRAPHY.</p>
  <div class="person">
    <div class="person-name">Toviran</div>
    <div class="person-role">Photographer</div>
  </div>
  <ul class="contacts">
    <li>
      <svg viewBox="0 0 24 24"><path fill="#fff" d="M6.6 10.8a15 15 0 0 0 6.6 6.6l2.2-2.2a1 1 0 0 1 1-.25 11.4 11.4 0 0 0 3.6.57 1 1 0 0 1 1 1V20a1 1 0 0 1-1 1A17 17 0 0 1 3 4a1 1 0 0 1 1-1h3.5a1 1 0 0 1 1 1c0 1.25.2 2.45.57 3.57a1 1 0 0 1-.25 1z"/></svg>
      : 0417395268
    </li>
    <li>
      <svg viewBox="0 0 24 24"><circle cx="12" cy="12" r="9" fill="none" stroke="#fff" stroke-width="2"/><path d="M3 12h18M12 3c3 3 3 15 0 18M12 3c-3 3-3 15 0 18" fill="none" stroke="#fff" stroke-width="1.5"/></svg>
      : www.kestrelphotography.com.au
    </li>
    <li>
      <span class="icon-square"></span>
      : kestrelphotography
    </li>
  </ul>
</section>

</body>
</html>
```